Business Card Design for Telecommunications and IT Solutions company "OKRA"

BC for telecommunications company name "OKRA" with slogan "Telecom & IT Solutions"

should have the full name as above "OKRA" and the slogan
color reqiured black, red (dark) and white

simple, professional, serious, modern design is required

1 side of business card have a full details, contacts and logo
other side have only the logo, website and full company name "ALOKRA Company for Telecommunications service & Information Technology LLC"

i have attached the logo and current business card sample and note that the logo was changed not the same in the attached business card

Industry/Entity Type

Telecommunications

Contact Information for Business Card

Full name: Omar Nabil Al Hudari
Job title: General Manager
Mobile no: +964xxxxxxxxx
email: omar@okra-tel.example
full name of the company: ALOKRA Company Telecommunications Services & Information Technology LLC.
website: www.okra-tel.example
address: Nakheel Dist. 148/7 JubailaQadim, Basra, Iraq

Requirements
Must have
• two languages in the same side of business card (English, Arabic) for only the name and title

```html
<!DOCTYPE html>
<html lang="en">
<head>
<meta charset="utf-8">
<title>OKRA Business Card</title>
<link href="https://fonts.googleapis.com/css2?family=Jost:wght@400;500&family=Open+Sans:wght@400;600&family=Noto+Kufi+Arabic:wght@400;500&display=swap" rel="stylesheet">
<style>
  :root {
    --backdrop: #8c8c8c;
    --card-black: #1b1b1b;
    --card-white: #f4f4f2;
    --brand-red: #a8201a;
    --ink-white: #ffffff;
    --ink-grey: #bdbdbd;
    --ink-black: #161616;
  }
  * { margin: 0; padding: 0; box-sizing: border-box; }
  html, body { width: 1200px; height: 1200px; overflow: hidden; }
  body {
    background: var(--backdrop);
    display: flex; flex-direction: column; align-items: center; justify-content: center;
    gap: 56px;
    font-family: "Open Sans", sans-serif;
  }
  .card {
    position: relative; width: 900px; height: 514px; overflow: hidden;
    box-shadow: 0 8px 24px rgba(0,0,0,.25);
  }

  /* Back side */
  .card--back { background: var(--card-white); }
  .back__brand { position: absolute; right: 150px; top: 52px; text-align: right; }
  .wordmark {
    font-family: "Jost", sans-serif; font-weight: 500; letter-spacing: 4px; line-height: 1;
  }
  .back__brand .wordmark { font-size: 88px; color: var(--ink-black); }
  .slogan {
    font-family: "Jost", sans-serif; font-size: 14px; letter-spacing: 1.5px; text-transform: uppercase;
  }
  .back__brand .slogan { color: var(--ink-black); margin-top: 4px; }
  .company-band {
    position: absolute; left: 0; right: 0; top: 190px; height: 116px;
    background: var(--card-black); color: var(--ink-white);
    font-family: "Jost", sans-serif; text-align: center;
    display: flex; flex-direction: column; justify-content: center;
  }
  .company-band__name { font-size: 30px; letter-spacing: 2px; }
  .company-band__full { font-size: 21px; letter-spacing: 1px; margin-top: 4px; }
  .company-arabic { position: absolute; left: 0; right: 0; top: 318px; text-align: center; font-family: "Noto Kufi Arabic", sans-serif; }
  .company-arabic__name { font-size: 26px; color: var(--ink-black); }
  .company-arabic__full { font-size: 24px; color: var(--brand-red); }
  .website-pill {
    position: absolute; left: 50%; bottom: -24px; transform: translateX(-50%);
    background: var(--brand-red); color: var(--ink-white);
    font-family: "Jost", sans-serif; font-size: 28px; letter-spacing: 1.5px;
    padding: 16px 44px 40px; border-radius: 28px; white-space: nowrap;
  }

  /* Front side */
  .card--front { background: var(--card-black); color: var(--ink-white); }
  .front__arcs { position: absolute; left: 0; top: 0; }
  .front__brand { position: absolute; left: 66px; top: 92px; }
  .front__brand .wordmark { font-size: 80px; color: var(--ink-white); }
  .front__brand .slogan { color: var(--ink-grey); text-align: right; margin-top: 4px; font-size: 13px; }
  .address {
    position: absolute; left: 44px; bottom: 28px;
    font-family: "Jost", sans-serif; font-size: 22px; line-height: 1.3; color: var(--ink-grey); letter-spacing: 1px;
    white-space: nowrap;
  }
  .person { position: absolute; right: 48px; top: 46px; text-align: right; }
  .person__name { font-size: 32px; letter-spacing: .5px; white-space: nowrap; }
  .person__title { font-family: "Jost", sans-serif; font-size: 19px; letter-spacing: 1.5px; color: var(--brand-red); text-transform: uppercase; }
  .contacts { position: absolute; right: 48px; top: 150px; font-size: 22px; line-height: 1.5; white-space: nowrap; }
  .contacts__label { color: var(--brand-red); display: inline-block; width: 92px; }
  .divider { position: absolute; left: 600px; top: 268px; width: 156px; height: 5px; background: var(--brand-red); border-radius: 3px; }
  .person-arabic { position: absolute; right: 48px; bottom: 44px; text-align: right; font-family: "Noto Kufi Arabic", sans-serif; }
  .person-arabic__name { font-size: 34px; }
  .person-arabic__title { font-size: 30px; color: var(--brand-red); }
</style>
</head>
<body>

  <section class="card card--back" aria-label="Business card, company side">
    <div class="back__brand">
      <div class="wordmark">OKRA</div>
      <div class="slogan">Telecom &amp; IT Solutions</div>
    </div>
    <div class="company-band">
      <div class="company-band__name">ALOKRA Company</div>
      <div class="company-band__full">for Telecommunications service &amp; Information Technology LLC</div>
    </div>
    <div class="company-arabic" dir="rtl" lang="ar">
      <div class="company-arabic__name">شركة أوكرا</div>
      <div class="company-arabic__full">لخدمات الإتصالات وتقنية المعلومات المحدودة</div>
    </div>
    <div class="website-pill">www.okra-tel.example</div>
  </section>

  <section class="card card--front" aria-label="Business card, contact side">
    <svg class="front__arcs" width="520" height="514" viewBox="0 0 520 514" aria-hidden="true">
      <path d="M430 0 A250 250 0 0 1 230 400 A270 270 0 0 0 430 0 Z" fill="#ffffff"/>
      <path d="M0 270 A215 215 0 0 0 390 150 A250 250 0 0 1 0 270 Z" fill="#a8201a"/>
    </svg>
    <div class="front__brand">
      <div class="wordmark">OKRA</div>
      <div class="slogan">Telecom &amp; IT Solutions</div>
    </div>
    <div class="address">Nakheel Dist. 148/7<br>JubailaQadim, Basra, Iraq</div>

    <div class="person">
      <div class="person__name">Omar Nabil Al Hudari</div>
      <div class="person__title">General Manager</div>
    </div>
    <div class="contacts">
      <div><span class="contacts__label">Mobile:</span>+964xxxxxxxxx</div>
      <div><span class="contacts__label">e-mail:</span>omar@okra-tel.example</div>
    </div>
    <div class="divider"></div>
    <div class="person-arabic" dir="rtl" lang="ar">
      <div class="person-arabic__name">عمر نبيل الحضري</div>
      <div class="person-arabic__title">المدير العام</div>
    </div>
  </section>

</body>
</html>
```